wine bottle label design

My girlfriend and I are getting married. We are sending out invitations, in a wine bottle. For that we need a label on the bottle.
Our names are Mette & Jørgen. We would like the M and J to somehow play a bigger part in the logo.
Also maybe with an Illustration (best if made as a drawing resembling the church we are getting married in) https://www.fjordtonerne.dk/index.php/kalender/83-uncategorised/148-gospelgudstjeneste-i-dalbro-kirke.html

Bryllup den 27 april 2019, kl. 14:00 i Dalbro Kirke

Decorative

```html
<!DOCTYPE html>
<html lang="da">
<head>
<meta charset="utf-8">
<title>Mette &amp; Jørgen – vinetiket</title>
<link rel="stylesheet" href="https://fonts.googleapis.com/css2?family=Great+Vibes&family=Cinzel:wght@400&display=swap">
<style>
  :root {
    --paper: #ffffff;
    --label: #f2eee7;
    --label-edge: #e6dfd4;
    --gold: #c2a687;
    --grey: #8b8e93;
    --mark: #1a1a1a;
  }
  html, body {
    margin: 0;
    padding: 0;
    overflow: hidden;
    background: var(--paper);
  }
  .canvas {
    position: relative;
    width: 1014px;
    height: 1200px;
    overflow: hidden;
    background: var(--paper);
  }
  .crop-marks {
    position: absolute;
    inset: 0;
  }
  .label {
    position: absolute;
    left: 54px;
    top: 54px;
    width: 906px;
    height: 1093px;
    background: radial-gradient(ellipse at center, #f7f4ef 0%, var(--label) 60%, var(--label-edge) 100%);
  }
  .damask {
    position: absolute;
    inset: 0;
  }
  .flourish {
    position: absolute;
    left: 182px;
    width: 542px;
    height: 87px;
    border-radius: 44px;
    background: radial-gradient(ellipse at center, rgba(194,166,135,0.55) 0%, rgba(194,166,135,0.25) 55%, rgba(194,166,135,0) 75%);
  }
  .flourish--top { top: 83px; }
  .flourish--bottom { top: 927px; }

  .monogram {
    position: absolute;
    inset: 0;
    font-family: "Great Vibes", cursive;
    line-height: 1;
  }
  .monogram span { position: absolute; white-space: nowrap; }
  .initial { color: var(--gold); font-size: 210px; }
  .rest { color: var(--grey); font-size: 92px; }
  .amp { color: var(--grey); font-size: 90px; }
  .initial--m { left: 250px; top: 190px; }
  .rest--m { left: 395px; top: 268px; }
  .amp { left: 288px; top: 375px; }
  .initial--j { left: 345px; top: 355px; }
  .rest--j { left: 460px; top: 440px; }

  .church {
    position: absolute;
    left: 198px;
    top: 509px;
    width: 506px;
    height: 257px;
    background: linear-gradient(to bottom, rgba(194,166,135,0.15) 0%, rgba(194,166,135,0.55) 100%);
    border-radius: 6px;
  }
  .church-base {
    position: absolute;
    left: 198px;
    top: 745px;
    width: 506px;
    height: 3px;
    background: var(--gold);
  }

  .details {
    position: absolute;
    left: 0;
    top: 806px;
    width: 906px;
    margin: 0;
    text-align: center;
    font-family: "Cinzel", serif;
    font-weight: 400;
    font-size: 31px;
    line-height: 44px;
    letter-spacing: 1px;
    color: var(--grey);
  }
</style>
</head>
<body>
<div class="canvas">
  <svg class="crop-marks" width="1014" height="1200" viewBox="0 0 1014 1200" aria-hidden="true">
    <g stroke="var(--mark)" stroke-width="1">
      <line x1="73" y1="0" x2="73" y2="51"/>
      <line x1="941" y1="0" x2="941" y2="51"/>
      <line x1="0" y1="71" x2="51" y2="71"/>
      <line x1="963" y1="71" x2="1014" y2="71"/>
      <line x1="0" y1="1128" x2="51" y2="1128"/>
      <line x1="963" y1="1128" x2="1014" y2="1128"/>
      <line x1="73" y1="1149" x2="73" y2="1200"/>
      <line x1="941" y1="1149" x2="941" y2="1200"/>
    </g>
  </svg>

  <div class="label">
    <div class="damask" role="img" aria-label="Faint cream damask pattern covering the label"></div>

    <div class="flourish flourish--top" role="img" aria-label="Gold scrolling flourish ornament"></div>

    <div class="monogram" aria-label="Mette &amp; Jørgen">
      <span class="initial initial--m">M</span>
      <span class="rest rest--m">ette</span>
      <span class="amp">&amp;</span>
      <span class="initial initial--j">J</span>
      <span class="rest rest--j">ørgen</span>
    </div>

    <div class="church" role="img" aria-label="Gold drawing of Dalbro Kirke with its tall tower on a small hill"></div>
    <div class="church-base"></div>

    <p class="details">Bryllup den 27 april 2019,<br>kl. 14:00 i Dalbro Kirke</p>

    <div class="flourish flourish--bottom" role="img" aria-label="Gold scrolling flourish ornament"></div>
  </div>
</div>
</body>
</html>
```